Cordova Exercise Phone Application Screen Design

We need a sharp professional design for a phone application. We specialize in Health and Fitness Software. This app will be a companion for www.VigorDeckNow.com.
We will be doing all backend and javascript work here and we need someone to create the HTML and CSS for the application which will be developed in Cordova.
For the contest we are submitting three screens. Once we award a winner we will give the winner the first oportunity to bid on the remaining 10 screens.
For the first step of the contest please do the page 1 and page 2 screen design, feel free to submit multiple designs. If we like your designs we will contact you and ask you to design the third page. Once that is done we would like to see the HTML and CSS for the three pages.
Page 1: Simple Home Page
Page 2: Client Search - The search is at the top and the results are below that. The Active | Inactive section is a selection (see https://quorblenet.com/radio-buttons-as-toggle-buttons-with-css/ for an example). Client A has their record expanded (that is what the triangle is). 136 stars should be 136 with Font-Awesome star after the number. To see what the graphs should look like please see the attached png. Then a list is below the stars and graphs.
Page 3/4: Step 1 of 3 - When the magnifying glass is selected a flyout with the search criteria comes out (page 3). Criteria is selected and the results are shown (page 4).
The default width should be 320 but the application should look good on all phones and tablets.
Please feel free to contact us with questions. The winner will get more work of a similar nature.

Target Market(s)
Physical Therapists
Colors
Designer to choose colors to be used in the design.
Requirements
Must have
- Clean and easy to understand design. Look professional and uncluttered. Be easy to understand and use. Must have the logo at the top (just the VDN logo is fine)
Should not have
- Cartoonish look and feel.

```html
<!DOCTYPE html>
<html lang="en">
<head>
<meta charset="utf-8">
<title>VigorDeckNow – Home</title>
<link href="https://fonts.googleapis.com/css2?family=Roboto:wght@400;500&display=swap" rel="stylesheet">
<style>
  :root {
    --page-bg: #3b3b3d;
    --screen-bg: #ffffff;
    --panel-bg: #f3f3f8;
    --card-bg: #ffffff;
    --ink: #111111;
    --label: #5b5f66;
    --badge: #e8262d;
    --help: #2196f3;
    --chat: #00897b;
    --protocol: #4caf50;
    --gear: #546e7a;
    --search-rim: #3a6f9a;
    --search-glass: #8fd0f5;
    --halo: #f0eef6;
    --bubble-in: #f4d8f8;
    --bubble-out: #fdf5fe;
  }
  * { box-sizing: border-box; margin: 0; padding: 0; }
  html, body { width: 1200px; height: 1200px; overflow: hidden; }
  body {
    background: var(--page-bg);
    font-family: "Roboto", sans-serif;
    position: relative;
  }
  .screen {
    position: absolute;
    left: 323px; top: 0;
    width: 554px; height: 1200px;
    background: var(--screen-bg);
    overflow: hidden;
  }
  .status-bar { position: absolute; left: 0; top: 0; width: 100%; height: 60px; }
  .status-time {
    position: absolute; left: 46px; top: 22px;
    font-size: 21px; font-weight: 500; color: var(--ink);
  }
  .status-icons { position: absolute; right: 22px; top: 24px; }

  .app-header { position: absolute; left: 0; top: 96px; width: 100%; height: 78px; }
  .brand-mark {
    position: absolute; left: 31px; top: 14px;
    font-size: 30px; font-weight: 500; letter-spacing: 4px;
    color: var(--ink); line-height: 1;
  }
  .app-title {
    position: absolute; left: 0; width: 100%; top: 22px;
    text-align: center; font-size: 25px; font-weight: 400; color: var(--ink);
  }
  .inbox { position: absolute; left: 426px; top: 20px; }
  .inbox-badge {
    position: absolute; left: 450px; top: 18px;
    width: 19px; height: 19px; border-radius: 50%;
    background: var(--badge); color: #fff;
    font-size: 13px; font-weight: 500; text-align: center; line-height: 19px;
  }
  .help-button {
    position: absolute; left: 490px; top: 20px;
    width: 32px; height: 32px; border-radius: 50%;
    background: var(--help); color: #fff;
    font-size: 22px; font-weight: 500; text-align: center; line-height: 32px;
  }

  .hero {
    position: absolute; left: 0; top: 174px; width: 100%; height: 340px;
    background: linear-gradient(180deg, #c9cbcc 0%, #8e8f90 45%, #2f2f31 100%);
  }
  .hero-dots { position: absolute; left: 251px; top: 310px; display: flex; gap: 6px; }
  .hero-dots span { width: 8px; height: 8px; border-radius: 50%; background: rgba(255,255,255,.45); }
  .hero-dots span.is-active { background: #ffffff; }

  .menu-panel {
    position: absolute; left: 0; top: 514px; width: 100%; height: 686px;
    background: var(--panel-bg);
  }
  .menu-card {
    position: absolute; width: 235px; height: 301px;
    background: var(--card-bg);
    box-shadow: 0 1px 3px rgba(0,0,0,.08);
  }
  .menu-card.search   { left: 31px;  top: 30px; }
  .menu-card.add      { left: 287px; top: 30px; }
  .menu-card.protocol { left: 31px;  top: 355px; }
  .menu-card.settings { left: 287px; top: 355px; }
  .menu-icon { position: absolute; left: 50%; transform: translateX(-50%); }
  .menu-label {
    position: absolute; left: 0; width: 100%;
    text-align: center; font-size: 21px; line-height: 35px; color: var(--label);
  }
  .search .menu-icon   { top: 56px; }
  .search .menu-label  { top: 138px; }
  .add .menu-icon      { top: 96px; }
  .add .menu-label     { top: 178px; }
  .protocol .menu-icon { top: 92px; }
  .protocol .menu-label{ top: 174px; }
  .settings .menu-icon { top: 92px; }
  .settings .menu-label{ top: 172px; }

  .messages-button {
    position: absolute; left: 178px; top: 246px;
    width: 196px; height: 196px; border-radius: 50%;
    background: var(--halo);
  }
  .messages-bubble {
    position: absolute; left: 20px; top: 20px;
    width: 156px; height: 156px; border-radius: 50%;
    background: radial-gradient(circle, var(--bubble-out) 30%, var(--bubble-in) 100%);
  }
  .messages-bubble svg { position: absolute; left: 59px; top: 29px; }
  .messages-label {
    position: absolute; left: 0; width: 100%; top: 82px;
    text-align: center; font-size: 21px; color: var(--label);
  }
</style>
</head>
<body>
  <main class="screen">
    <div class="status-bar">
      <span class="status-time">9:41</span>
      <svg class="status-icons" width="100" height="18" viewBox="0 0 100 18" aria-hidden="true">
        <rect x="0" y="12" width="4" height="6" fill="#111"/>
        <rect x="6" y="9" width="4" height="9" fill="#111"/>
        <rect x="12" y="5" width="4" height="13" fill="#111"/>
        <rect x="18" y="1" width="4" height="17" fill="#111"/>
        <path d="M30 6 a14 14 0 0 1 20 0 l-2 2 a11 11 0 0 0 -16 0z M34 10 a8 8 0 0 1 12 0 l-2 2 a5 5 0 0 0 -8 0z" fill="#111"/>
        <circle cx="40" cy="15" r="2" fill="#111"/>
        <rect x="62" y="2" width="32" height="15" rx="4" fill="none" stroke="#111" stroke-width="1.5"/>
        <rect x="64.5" y="4.5" width="27" height="10" rx="2" fill="#111"/>
        <rect x="95.5" y="7" width="2.5" height="5" rx="1" fill="#111"/>
      </svg>
    </div>

    <header class="app-header">
      <span class="brand-mark">VDN</span>
      <h1 class="app-title">VIGOR DECK NOW</h1>
      <svg class="inbox" width="32" height="24" viewBox="0 0 32 24" aria-label="Inbox">
        <rect x="1" y="3" width="30" height="20" rx="2" fill="#e3e7ea" stroke="#b8c0c6"/>
        <path d="M1 4 L16 15 L31 4" fill="none" stroke="#9aa4ab" stroke-width="1.5"/>
      </svg>
      <span class="inbox-badge">2</span>
      <span class="help-button">?</span>
    </header>

    <section class="hero" role="img" aria-label="Photo of a woman doing a floor exercise in a gym">
      <div class="hero-dots">
        <span></span><span class="is-active"></span><span></span><span></span><span></span>
      </div>
    </section>

    <section class="menu-panel">
      <a class="menu-card search">
        <svg class="menu-icon" width="44" height="44" viewBox="0 0 44 44" aria-hidden="true">
          <circle cx="18" cy="18" r="14" fill="var(--search-glass)" stroke="var(--search-rim)" stroke-width="3"/>
          <line x1="28" y1="28" x2="40" y2="40" stroke="var(--search-rim)" stroke-width="5" stroke-linecap="round"/>
        </svg>
        <p class="menu-label">Search for Clients<br>/Create Exercise<br>Program</p>
      </a>
      <a class="menu-card add">
        <svg class="menu-icon" width="42" height="42" viewBox="0 0 42 42" aria-hidden="true">
          <path d="M2 10 V2 H10 M32 2 H40 V10 M40 32 V40 H32 M10 40 H2 V32" fill="none" stroke="#2e7d32" stroke-width="2.5"/>
          <circle cx="21" cy="16" r="7" fill="#9e9e9e"/>
          <path d="M8 38 a13 11 0 0 1 26 0z" fill="#5c6bc0"/>
        </svg>
        <p class="menu-label">Add Client</p>
      </a>
      <a class="menu-card protocol">
        <svg class="menu-icon" width="40" height="40" viewBox="0 0 40 40" aria-hidden="true">
          <rect width="40" height="40" rx="3" fill="var(--protocol)"/>
          <path d="M20 6 L27 14 H22 V26 H27 L20 34 L13 26 H18 V14 H13z" fill="#fff"/>
        </svg>
        <p class="menu-label">Protocols</p>
      </a>
      <a class="menu-card settings">
        <svg class="menu-icon" width="42" height="42" viewBox="0 0 42 42" aria-hidden="true">
          <g fill="var(--gear)">
            <circle cx="21" cy="21" r="14"/>
            <rect x="17" y="1" width="8" height="40" rx="2"/>
            <rect x="17" y="1" width="8" height="40" rx="2" transform="rotate(45 21 21)"/>
            <rect x="17" y="1" width="8" height="40" rx="2" transform="rotate(90 21 21)"/>
            <rect x="17" y="1" width="8" height="40" rx="2" transform="rotate(135 21 21)"/>
          </g>
          <circle cx="21" cy="21" r="6" fill="#fff"/>
        </svg>
        <p class="menu-label">Settings</p>
      </a>

      <a class="messages-button">
        <div class="messages-bubble">
          <svg width="38" height="40" viewBox="0 0 38 40" aria-hidden="true">
            <path d="M4 0 H34 a4 4 0 0 1 4 4 V26 a4 4 0 0 1 -4 4 H10 L2 38 V4 a4 4 0 0 1 2 -4z" fill="var(--chat)"/>
            <circle cx="11" cy="15" r="2.6" fill="#fff"/>
            <circle cx="19" cy="15" r="2.6" fill="#fff"/>
            <circle cx="27" cy="15" r="2.6" fill="#fff"/>
          </svg>
          <span class="messages-label">Messages</span>
        </div>
      </a>
    </section>
  </main>
</body>
</html>
```